Brookhaven Business Card

I would like to re-design my company business card. I have my main company logo (Brookhaven) which must remain unchanged and I also have a number of product brands which I would like to also show on the card in some way. The corporate company colors are Blue and Orange, see pantone colors on file. However, it is not necessary to use these colors thoroughout. I am ok with grey tones etc...

Target Market(s)

Trade Business

Industry/Entity Type

Furniture

Contact Information for Business Card

Needs to incorporate Brookhaven as the main Logo. The Torvel and Kandrel product brands within the company. These can be on the back of the card.

Font styles to use
Sans Serif

Colors
0355a3
f37122

Requirements
Must have
• Marco Velditch
• COO (Global)
• Brookhaven Pacific Holdings Inc. (4371)
• Level 3, 47 Harlow Street, Melbourne VIC 3000 Australia
• Tel: +61 3 9481 2736 Mobile: +61 427 586 204
• e-mail: marco@brookhaven-au.example
• web: www.brookhaven-au.example
Nice to have
• Should be a corporate
Should not have
• No images of furniture

```html
<!DOCTYPE html>
<html lang="en">
<head>
<meta charset="utf-8">
<title>Brookhaven Business Card</title>
<link href="https://fonts.googleapis.com/css2?family=Ubuntu:wght@400;500&family=Arimo:wght@400&display=swap" rel="stylesheet">
<style>
  :root {
    --brand-blue: #2f5cb0;
    --brand-orange: #e0822a;
    --card-black: #000000;
    --card-white: #ffffff;
    --ink-navy: #0d1a3a;
    --stage: #e9e7e3;
  }
  * { box-sizing: border-box; margin: 0; padding: 0; }
  html, body { width: 1200px; height: 902px; overflow: hidden; }
  body {
    background: var(--stage);
    position: relative;
    font-family: "Ubuntu", sans-serif;
  }
  .card {
    position: absolute;
    left: 250px;
    width: 700px;
    height: 389px;
    overflow: hidden;
    box-shadow: 0 6px 18px rgba(0,0,0,0.18);
  }
  .card-back { top: 36px; background: var(--card-white); }
  .card-front { top: 477px; background: var(--card-white); }

  .brand-lockup {
    position: absolute;
    display: flex;
    align-items: center;
  }
  .brand-mark {
    display: block;
    background: var(--brand-orange);
    border-radius: 8px;
  }
  .brand-name {
    font-family: "Ubuntu", sans-serif;
    font-weight: 500;
    color: var(--brand-blue);
    letter-spacing: -1.5px;
    line-height: 1;
  }
  .card-back .brand-lockup { left: 118px; top: 148px; gap: 22px; }
  .card-back .brand-mark { width: 86px; height: 86px; border-radius: 12px; }
  .card-back .brand-name { font-size: 86px; }

  .front-shapes { position: absolute; inset: 0; }
  .card-front .brand-lockup { left: 36px; top: 62px; gap: 14px; }
  .card-front .brand-mark { width: 56px; height: 56px; }
  .card-front .brand-name { font-size: 56px; }

  .person { position: absolute; left: 60px; top: 248px; }
  .person-name {
    font-family: "Ubuntu", sans-serif;
    font-weight: 500;
    font-size: 33px;
    color: var(--brand-blue);
  }
  .person-title {
    font-family: "Ubuntu", sans-serif;
    font-size: 19px;
    color: var(--card-white);
    margin-top: 2px;
  }

  .contact-list {
    position: absolute;
    right: 20px;
    top: 178px;
    list-style: none;
    font-family: "Arimo", sans-serif;
    font-size: 14px;
    color: var(--ink-navy);
    text-align: right;
  }
  .contact-list li {
    display: flex;
    justify-content: flex-end;
    align-items: center;
    gap: 10px;
    height: 26px;
  }
  .contact-icon { width: 18px; height: 18px; fill: var(--card-white); stroke: var(--card-white); }
  .address {
    position: absolute;
    right: 20px;
    bottom: 18px;
    font-family: "Arimo", sans-serif;
    font-size: 14px;
    color: var(--ink-navy);
  }
</style>
</head>
<body>

  <section class="card card-back" aria-label="Card back">
    <div class="brand-lockup">
      <span class="brand-mark"></span>
      <span class="brand-name">Brookhaven</span>
    </div>
  </section>

  <section class="card card-front" aria-label="Card front">
    <svg class="front-shapes" width="700" height="389" viewBox="0 0 700 389" aria-hidden="true">
      <path d="M0 0 H545 Q540 300 0 389 Z" fill="var(--card-black)"/>
      <path d="M700 0 Q600 300 25 389 H700 Z" fill="var(--brand-blue)"/>
    </svg>

    <div class="brand-lockup">
      <span class="brand-mark"></span>
      <span class="brand-name">Brookhaven</span>
    </div>

    <div class="person">
      <p class="person-name">Marco Velditch</p>
      <p class="person-title">COO (Global)</p>
    </div>

    <ul class="contact-list">
      <li>+61 427 586 204
        <svg class="contact-icon" viewBox="0 0 18 18"><circle cx="9" cy="5" r="4" stroke="none"/><path d="M1 17 Q9 6 17 17 Z" stroke="none"/></svg>
      </li>
      <li>+61 3 9481 2736
        <svg class="contact-icon" viewBox="0 0 18 18"><rect x="3" y="1" width="12" height="16" fill="none" stroke-width="2"/><path d="M6 5h2M10 5h2M6 9h2M10 9h2M6 13h2M10 13h2" stroke-width="2"/></svg>
      </li>
      <li>marco@brookhaven-au.example
        <svg class="contact-icon" viewBox="0 0 18 18"><rect x="1" y="4" width="16" height="11" fill="none" stroke-width="1.6"/><path d="M1 4 L9 11 L17 4" fill="none" stroke-width="1.6"/></svg>
      </li>
      <li>www.brookhaven-au.example
        <svg class="contact-icon" viewBox="0 0 18 18"><rect x="1" y="2" width="16" height="11" fill="none" stroke-width="1.6"/><path d="M6 17h6M9 13v4" fill="none" stroke-width="1.6"/></svg>
      </li>
    </ul>

    <p class="address">Level 3, 47 Harlow Street, Melbourne VIC 3000 Australia</p>
  </section>

</body>
</html>
```